International industry company needs New Email Marketing Design

We need a new Email Marketing Design with the content in the attachment (html file).

Target Market(s)

engineers, technical directors, technologists, scientists from the aviation, defense, space and energy industries.

Font styles to use
Sans Serif

Requirements
Must have
• vexa.flanges logo
photo of a gas turbine.
Should not have
• it cannot contain elements indicating material testing

```html
<!DOCTYPE html>
<html lang="en">
<head>
<meta charset="utf-8">
<title>vexa.flanges – Precision Machining of Aerospace Components</title>
<link href="https://fonts.googleapis.com/css2?family=Arimo:wght@400;700&family=Nunito+Sans:wght@400&display=swap" rel="stylesheet">
<style>
  :root {
    --page-bg: #f2f6f9;
    --brand-blue: #3a56a0;
    --brand-gold: #dfa033;
    --white: #ffffff;
    --ink: #111111;
    --list-ink: #1a1a1a;
  }
  html, body {
    margin: 0;
    padding: 0;
    width: 741px;
    height: 1200px;
    overflow: hidden;
    background: var(--page-bg);
  }
  .email {
    position: relative;
    width: 741px;
    height: 1200px;
    font-family: Arimo, Arial, sans-serif;
  }
  .column {
    position: absolute;
    left: 208px;
    width: 325px;
  }
  .brand-bar {
    top: 5px; height: 45px;
    background: var(--white);
    border-top: 1.5px solid var(--brand-blue);
    display: flex; align-items: center; justify-content: center;
  }
  .brand-name {
    font-weight: 700; font-size: 27px; color: var(--brand-blue);
    letter-spacing: 0.3px;
  }
  .hero-title {
    top: 50px; height: 86px; margin: 0;
    background: var(--brand-blue); color: var(--white);
    display: flex; align-items: center; justify-content: center;
    text-align: center; font-weight: 700; font-size: 16.6px; line-height: 26px;
    letter-spacing: -0.4px;
  }
  .hero-photo {
    top: 136px; height: 177px;
    background: linear-gradient(180deg, #6b6f78 0%, #b3a98f 40%, #8b8a8a 70%, #3f4a6e 100%);
  }
  .intro {
    top: 313px; height: 133px;
    background: var(--brand-blue); color: var(--white); text-align: center;
  }
  .intro-greeting { margin: 10px 0 10px; font-size: 14.6px; font-weight: 400; }
  .intro-text { margin: 0 3px; font-size: 9.1px; line-height: 13.5px; }
  .experience-band {
    top: 451px; height: 58px; margin: 0;
    background: var(--brand-gold); color: var(--white);
    display: flex; align-items: center; justify-content: center;
    text-align: center; font-weight: 700; font-size: 14.2px; line-height: 21px;
    letter-spacing: -0.3px;
  }
  .experience {
    top: 509px; height: 272px; background: var(--white);
  }
  .bullet-list {
    list-style: none; margin: 0; padding: 0;
    font-family: "Nunito Sans", Arial, sans-serif;
    font-size: 8.6px; line-height: 13px;
  }
  .bullet-list li { position: relative; padding-left: 8px; }
  .bullet-list li::before {
    content: ""; position: absolute; left: 0; top: 7px;
    width: 1.5px; height: 1.5px; background: currentColor;
  }
  .experience .bullet-list {
    position: absolute; left: 23px; top: 30px; width: 124px; color: var(--list-ink);
  }
  .parts-photo {
    position: absolute; left: 172px; top: 14px; width: 133px; height: 155px;
    background: linear-gradient(135deg, #f4f4f4 0%, #c9cbce 55%, #9da0a4 100%);
    border-radius: 4px;
  }
  .read-more {
    position: absolute; left: 11px; top: 228px; width: 303px; height: 28px;
    background: var(--brand-gold); border-radius: 3px;
    color: var(--white); font-family: "Nunito Sans", Arial, sans-serif;
    font-size: 9.2px; line-height: 9px; text-align: center;
    display: flex; flex-direction: column; justify-content: center;
    text-decoration: none;
  }
  .accessories {
    top: 781px; height: 177px; background: var(--brand-blue); color: var(--white);
  }
  .fixture-photo {
    position: absolute; left: 28px; top: 30px; width: 106px; height: 114px;
    background: linear-gradient(135deg, #e6e8ea 0%, #a9adb3 60%, #7c8188 100%);
    border-radius: 4px;
  }
  .accessories-title {
    position: absolute; left: 178px; top: 13px; margin: 0;
    font-size: 9.4px; font-weight: 700; letter-spacing: -0.3px;
  }
  .accessories-lead {
    position: absolute; left: 171px; top: 35px; width: 145px; margin: 0;
    font-size: 9.4px; line-height: 14.5px;
  }
  .accessories .bullet-list {
    position: absolute; left: 184px; top: 79px; width: 124px;
  }
  .contact-line {
    position: absolute; left: 216px; top: 969px; margin: 0;
    font-size: 10.6px; color: var(--ink); letter-spacing: -0.2px;
  }
  .address {
    position: absolute; left: 208px; top: 1005px; width: 163px; height: 88px;
    background: var(--brand-blue); color: var(--white);
    font-size: 8px; line-height: 12px; font-style: normal;
    box-sizing: border-box; padding: 7px 0 0 8px;
  }
  .company-mark {
    position: absolute; left: 372px; top: 1005px; width: 160px; height: 88px;
    background: var(--white);
  }
  .company-mark svg { position: absolute; left: 0; top: 0; }
  .company-name {
    position: absolute; left: 56px; top: 38px; width: 100px; text-align: center;
    font-size: 11.5px; font-weight: 700; color: var(--brand-blue); letter-spacing: 0.4px;
  }
  .social {
    position: absolute; left: 338px; top: 1110px; display: flex; gap: 4px;
  }
  .social-link {
    width: 28px; height: 28px; border-radius: 50%; box-sizing: border-box;
    display: flex; align-items: center; justify-content: center;
    font-size: 8px; font-weight: 700; text-decoration: none;
  }
  .social-link.pro { border: 1.5px solid var(--brand-blue); color: var(--brand-blue); }
  .social-link.vid { border: 1.5px solid #d9252a; color: #d9252a; }
  .site-band {
    top: 1158px; height: 32px; background: var(--brand-gold);
    display: flex; align-items: center; justify-content: center;
  }
  .site-band a { color: var(--ink); font-size: 10.6px; text-decoration: underline; }
</style>
</head>
<body>
<div class="email">
  <header class="column brand-bar"><span class="brand-name">vexa.flanges</span></header>

  <h1 class="column hero-title">Precision Machining of Parts &amp;<br>Aerospace Components</h1>

  <div class="column hero-photo" role="img" aria-label="Photo of a large gas turbine rotor in an industrial hall"></div>

  <section class="column intro">
    <h2 class="intro-greeting">Dear Surface Coating Guild Members,</h2>
    <p class="intro-text">Dravontek manufactures high quality precision parts, flanges, rings, buttons, panels, discs, and strips for Thermal and Cold Spray facilities mainly in the aviation industry. We specialize in cutting difficult-to-machine aerospace grade materials such as nickel &amp; cobalt base superalloys, titanium, and hardened steel.</p>
  </section>

  <h2 class="column experience-band">Our experience includes manufacturing<br>components used in:</h2>

  <section class="column experience">
    <ul class="bullet-list">
      <li>Gas turbine engine hot section assemblies</li>
      <li>Compressor hardware</li>
      <li>Turbine blade roots</li>
      <li>Combustor liners and rings</li>
      <li>Shaft and bearing seats</li>
      <li>Flanges and casings</li>
      <li>Seal segments</li>
      <li>Nozzle guide vanes</li>
      <li>Satellite structures</li>
      <li>Defense drive systems</li>
      <li>Power generation rotors and stators</li>
    </ul>
    <div class="parts-photo" role="img" aria-label="Machined metal parts: threaded bar, flat strip, disc and small plates"></div>
    <a class="read-more" href="#"><span>Read more about our precision machined parts and components</span><span>here!</span></a>
  </section>

  <section class="column accessories">
    <div class="fixture-photo" role="img" aria-label="Machined metal multi-slot holding fixture"></div>
    <h3 class="accessories-title">Custom Workshop Accessories</h3>
    <p class="accessories-lead">Machining of production related tools:</p>
    <ul class="bullet-list">
      <li>Gravity or pressure type V-grooved holding fixture for batch spray coating of parts</li>
      <li>Masking fixture</li>
      <li>and more...</li>
    </ul>
  </section>

  <p class="contact-line">Do not hesitate to contact us, if you have any questions.</p>

  <address class="address">
    Dravontek Sp. z o.o.<br>
    Science and Technology Park 'Mirow'<br>
    Kalinowa 12 bud. 4C street<br>
    06-210 Lesno, Poland<br>
    phone: +48 500 123 456<br>
    email: info@dravontek.com
  </address>

  <div class="company-mark">
    <svg width="160" height="88" viewBox="0 0 160 88" aria-hidden="true">
      <polygon points="0,0 59,88 0,88" fill="var(--brand-blue)"/>
    </svg>
    <span class="company-name">DRAVONTEK</span>
  </div>

  <nav class="social">
    <a class="social-link pro" href="#">Pro</a>
    <a class="social-link vid" href="#">Vid</a>
  </nav>

  <footer class="column site-band"><a href="#">www.dravontek.com</a></footer>
</div>
</body>
</html>
```